Vela Habitat Real estate Costa del sol

we need a website for our Company based in Costa del sol, Spain. We sell properties on the spanish coast that is called costa del sol. We are concentrating on exclusive properties and would like the webdesign to show this. In our website we want to have area descriptions of the different areas we sell our Products. We will also implement a searchable database delivered by a third part where all properties for sale in Spain are listed. When looking into the designs we would like our main page to have a overview of the coast where the different areas are shown. Have a look at brightlomaview.com or ourtesa.com to see. The webpage will be presented in 4 languages, English, spanish, Swedish and norwegian, and shall of course also be prepared for social medias. We want an easy Contemporary design but still with an exclusive feeling!
Target Market(s)
Scandinavian and North european Citizens wants to buy a property in Spain
Industry/Entity Type
Real Estate
Number of Pages Required
5+ page
Look and feel

```html
<!DOCTYPE html>
<html lang="en">
<head>
<meta charset="utf-8">
<title>Vela Habitat – Costa del Sol Properties</title>
<link href="https://fonts.googleapis.com/css2?family=Roboto:wght@300;400;500;700&family=Roboto+Condensed:wght@400;700&display=swap" rel="stylesheet">
<style>
:root{
  --blue:#1677c4;
  --blue-dark:#1565a8;
  --navy:#0b1058;
  --orange:#f47a1f;
  --ink:#222;
  --muted:#6b6b6b;
  --grey-band:#a7adb1;
  --footer:#1b1b1b;
  --white:#fff;
}
*{box-sizing:border-box;margin:0;padding:0}
html,body{width:1200px;height:3429px;overflow:hidden}
body{position:relative;font-family:'Roboto',sans-serif;color:var(--ink);background:var(--white)}

/* header */
.site-header{position:absolute;left:0;top:0;width:1200px;height:149px;background:var(--white)}
.brand{position:absolute;left:98px;top:40px;display:flex;align-items:center;gap:12px}
.brand-mark{width:34px;height:34px;border:4px solid #333}
.brand-name{font-size:30px;font-weight:400;color:#333}
.question{position:absolute;left:500px;top:27px;width:186px;text-align:right;white-space:nowrap}
.question .q{font-size:16px;line-height:20px;color:#333}
.question .tel{font-size:16px;line-height:20px;font-weight:700;color:var(--blue-dark);margin-top:3px}
.phone-badge{position:absolute;left:698px;top:32px;width:36px;height:36px;border-radius:50%;background:var(--blue-dark)}
.langs{position:absolute;left:762px;top:43px;display:flex;gap:20px;font-size:11px;color:#333}
.langs span{display:flex;align-items:center;gap:5px}
.flag{width:15px;height:10px;display:inline-block}
.main-nav{position:absolute;left:300px;top:103px;width:900px;height:46px;background:var(--blue);clip-path:polygon(40px 0,100% 0,100% 100%,0 100%)}
.main-nav ul{list-style:none;display:flex;position:absolute;left:60px;top:0;height:46px;align-items:center}
.main-nav li{color:var(--white);font-size:12.5px;font-weight:500;padding:0 22px}

/* hero */
.hero{position:absolute;left:0;top:149px;width:1200px;height:528px;
  background:linear-gradient(180deg,#a4a9b7 0%,#c9b9b2 24%,#7a7f93 38%,#3b4766 55%,#223656 75%,#1d2c47 100%)}
.hero-title{position:absolute;left:766px;top:205px;font-family:'Roboto Condensed',sans-serif;font-weight:700;font-size:48px;line-height:50px;color:var(--white)}
.hero-sub{position:absolute;left:766px;top:310px;width:360px;font-size:15px;line-height:20px;color:var(--white)}
.hero-arrow{position:absolute;top:264px;width:34px;height:34px;border-radius:50%;background:rgba(0,0,0,.55)}

/* search */
.search-band{position:absolute;left:0;top:677px;width:1200px;height:157px;background:var(--navy)}
.search-band .notch{position:absolute;left:581px;top:-18px;width:0;height:0;border-left:18px solid transparent;border-right:18px solid transparent;border-bottom:18px solid var(--navy)}
.field{position:absolute;height:37px;width:220px;background:var(--white);font-size:12px;color:#777;padding:11px 12px;font-style:italic}
.field.select::after{content:"";position:absolute;right:12px;top:16px;border-left:5px solid transparent;border-right:5px solid transparent;border-top:6px solid #444}
.search-btn{position:absolute;left:837px;top:86px;width:221px;height:37px;background:var(--orange);color:var(--white);font-size:14px;font-weight:700;display:flex;align-items:center;justify-content:center;gap:6px}

.section-title{position:absolute;left:0;width:1200px;text-align:center;font-size:31px;font-weight:400;color:#222}

/* new properties */
.prop-card{position:absolute;top:944px;width:237px;height:249px;background:var(--blue)}
.prop-card .photo{height:187px}
.prop-card .price{position:absolute;left:70px;top:151px;width:97px;height:36px;background:var(--blue);color:var(--white);font-size:15px;display:flex;align-items:center;justify-content:center}
.prop-card p{color:var(--white);font-size:11.5px;line-height:16px;text-align:center;padding:14px 16px 0}

/* promoted */
.promo-head{position:absolute;left:0;top:1260px;width:1200px;height:70px;background:var(--grey-band);color:var(--white);font-family:'Roboto Condensed',sans-serif;font-weight:700;font-size:24px;text-align:center;line-height:76px}
.promo-photo{position:absolute;top:1330px;height:394px}
.promo-panel{position:absolute;left:402px;top:1330px;width:398px;height:394px;background:#9da3a6;color:var(--white);text-align:center;padding-top:80px}
.promo-panel h3{font-family:'Roboto Condensed',sans-serif;font-weight:700;font-size:31px;line-height:36px}
.promo-panel .lead{font-size:14px;line-height:20px;margin:14px 40px 0}
.promo-panel .facts{font-size:15px;line-height:20px;margin-top:14px}
.promo-panel .amount{font-size:29px;font-weight:700;margin-top:12px}
.promo-arrow{position:absolute;top:1500px;width:24px;height:40px}

/* highlighted */
.hl-item{position:absolute;width:330px;height:114px}
.hl-item .thumb{position:absolute;left:0;top:0;width:119px;height:114px}
.hl-item .txt{position:absolute;left:135px;top:-2px;width:190px}
.hl-item h4{font-size:16.5px;font-weight:400;color:#222;white-space:nowrap}
.hl-item .p{font-size:15px;color:var(--blue);margin-top:5px}
.hl-item .d{font-size:12px;line-height:17px;color:#555;margin-top:7px}

/* coast map */
.coast{position:absolute;left:0;top:2194px;width:1200px;height:503px;
  background:linear-gradient(180deg,#2c3556 0%,#3a4466 35%,#25304f 65%,#1c2744 100%)}
.marker{position:absolute;transform:translate(-50%,-50%);background:#0f1424;color:var(--white);font-size:12px;padding:5px 10px;white-space:nowrap;border:1px solid rgba(255,255,255,.5)}
.marker::after{content:"";position:absolute;left:50%;bottom:-6px;margin-left:-5px;border-left:5px solid transparent;border-right:5px solid transparent;border-top:6px solid #0f1424}

/* news */
.news{position:absolute;left:0;top:2697px;width:1200px;height:405px;background:#fbfbfb}
.news h2{position:absolute;left:98px;top:64px;font-size:27px;font-weight:400;color:#222}
.news-item{position:absolute;top:140px;width:320px}
.news-item h5{font-size:17px;font-weight:400;color:#333}
.news-item .date{font-size:15px;color:var(--orange);margin-top:10px}
.news-item .body{font-size:12px;line-height:19px;color:#666;margin-top:10px}
.news-item .more{font-size:11.5px;color:#555;margin-top:18px;display:flex;align-items:center;gap:6px}
.testimonial-title{position:absolute;left:784px;top:78px;font-size:20px;font-weight:400;color:#333}
.testimonial{position:absolute;left:784px;top:117px;width:318px;height:181px;background:var(--orange);color:var(--white);padding:26px 20px}
.testimonial q{display:block;font-size:11.5px;line-height:18px;font-style:italic}
.testimonial .who{font-size:12px;font-style:italic;margin-top:12px;padding-left:120px;line-height:17px}
.avatar{position:absolute;left:811px;top:265px;width:78px;height:78px;border-radius:50%;background:linear-gradient(135deg,#c9a189,#7f6a5e);border:4px solid #e9e9e9}

/* footer */
.site-footer{position:absolute;left:0;top:3102px;width:1200px;height:272px;background:var(--footer);color:var(--white)}
.foot-brand{position:absolute;left:98px;top:80px;display:flex;align-items:center;gap:10px}
.foot-brand .mark{width:30px;height:30px;border:4px solid var(--white)}
.foot-brand .name{font-size:28px;font-weight:400}
.socials{position:absolute;left:118px;top:175px;display:flex;gap:6px}
.socials span{width:20px;height:20px;border-radius:50%;border:1.5px solid var(--white)}
.foot-col{position:absolute;top:62px}
.foot-col h6{font-size:14px;font-weight:500;margin-bottom:14px}
.foot-col .line{font-size:12.5px;line-height:19px}
.foot-col .ico{display:flex;align-items:center;gap:14px;font-size:12.5px;margin-top:14px}
.quick li{list-style:none;font-size:12.5px;line-height:25px}
.email-input{width:229px;height:41px;background:var(--white);color:#777;font-size:11px;padding:14px 10px;margin-top:14px}
.subscribe{width:98px;height:34px;background:var(--blue);font-size:12px;display:flex;align-items:center;justify-content:center;margin-top:13px}
.copy-bar{position:absolute;left:0;top:3374px;width:1200px;height:55px;background:var(--blue-dark);color:var(--white);font-size:12px;text-align:center;line-height:55px}
</style>
</head>
<body>

<header class="site-header">
  <div class="brand"><span class="brand-mark"></span><span class="brand-name">Vela Habitat</span></div>
  <div class="question"><div class="q">Have any Question?</div><div class="tel">+1 505-555-0148</div></div>
  <div class="phone-badge">
    <svg width="36" height="36" viewBox="0 0 36 36"><path d="M13 11c1-1 2-1 3 0l2 3c.5 1 0 2-1 2.5-.5.5 0 2 2 4s3.5 2.5 4 2c.5-1 1.5-1.5 2.5-1l3 2c1 1 1 2 0 3-2 2-5 2-10-3s-7.5-8.5-5.5-10.5z" fill="#fff"/></svg>
  </div>
  <div class="langs">
    <span><i class="flag" style="background:linear-gradient(#c8102e 0 0) center/100% 3px no-repeat,linear-gradient(#c8102e 0 0) center/3px 100% no-repeat,#1f3f8f"></i>ENGLISH</span>
    <span><i class="flag" style="background:linear-gradient(#c60b1e 0 25%,#ffc400 25% 75%,#c60b1e 75%)"></i>SPANISH</span>
    <span><i class="flag" style="background:linear-gradient(#fecc00 0 0) 5px 0/3px 100% no-repeat,linear-gradient(#fecc00 0 0) 0 center/100% 2px no-repeat,#006aa7"></i>SWEDISH</span>
    <span><i class="flag" style="background:linear-gradient(#00205b 0 0) 5px 0/2px 100% no-repeat,linear-gradient(#00205b 0 0) 0 center/100% 2px no-repeat,linear-gradient(#fff 0 0) 4px 0/4px 100% no-repeat,linear-gradient(#fff 0 0) 0 center/100% 4px no-repeat,#ba0c2f"></i>NORWEGIAN</span>
  </div>
  <nav class="main-nav"><ul>
    <li>HOMES</li><li>ABOUT US</li><li>COSTA DEL SOL</li><li>SERVICES</li><li>PROPERTIES</li><li>BLOG</li><li>CONTACT US</li>
  </ul></nav>
</header>

<section class="hero" role="img" aria-label="Evening view over a harbour town on the coast with boats in the bay">
  <h1 class="hero-title">VELA HABITAT<br>PROPERTIES</h1>
  <p class="hero-sub">Lorem ipsum dolor sit amet, consectetur adipiscing sed do eiusmod tempor incididunt ut labore</p>
  <div class="hero-arrow" style="left:33px"><svg width="34" height="34"><path d="M20 11l-6 6 6 6" stroke="#fff" stroke-width="2.5" fill="none"/></svg></div>
  <div class="hero-arrow" style="left:1131px"><svg width="34" height="34"><path d="M14 11l6 6-6 6" stroke="#fff" stroke-width="2.5" fill="none"/></svg></div>
</section>

<section class="search-band">
  <span class="notch"></span>
  <div class="field select" style="left:142px;top:39px">Select one or more locations</div>
  <div class="field select" style="left:375px;top:39px">All types</div>
  <div class="field select" style="left:608px;top:39px">Min price</div>
  <div class="field" style="left:837px;top:39px;width:221px">Phone No</div>
  <div class="field select" style="left:142px;top:86px">Min beds</div>
  <div class="field select" style="left:375px;top:86px">subtype</div>
  <div class="field select" style="left:608px;top:86px">Unlimited</div>
  <div class="search-btn">SEARCH <svg width="14" height="14"><circle cx="7" cy="7" r="6" fill="none" stroke="#fff" stroke-width="1.6"/><path d="M6 4l3 3-3 3" stroke="#fff" stroke-width="1.6" fill="none"/></svg></div>
</section>

<h2 class="section-title" style="top:866px">NEW PROPERTIES</h2>
<article class="prop-card" style="left:98px"><div class="photo" role="img" aria-label="Modern villa with pool at dusk" style="background:linear-gradient(180deg,#7da6cf,#c9c2b5 55%,#3e7fa6)"></div><span class="price">265.000 €</span><p>Lorem ipsum dolor sit amet, consectetur adipiscing elit, sed do eiusmod</p></article>
<article class="prop-card" style="left:352px"><div class="photo" role="img" aria-label="Lit contemporary house at night" style="background:linear-gradient(180deg,#1e2a3c,#5b5346 55%,#b08a52)"></div><span class="price">265.000 €</span><p>Lorem ipsum dolor sit amet, consectetur adipiscing elit, sed do eiusmod</p></article>
<article class="prop-card" style="left:608px"><div class="photo" role="img" aria-label="White cubic villa under blue sky" style="background:linear-gradient(180deg,#5f93c9,#e8ecef 50%,#9aa4ad)"></div><span class="price">265.000 €</span><p>Lorem ipsum dolor sit amet, consectetur adipiscing elit, sed do eiusmod</p></article>
<article class="prop-card" style="left:864px"><div class="photo" role="img" aria-label="Villa with illuminated pool in the evening" style="background:linear-gradient(180deg,#203a5c,#8a5a3c 55%,#2a7fa8)"></div><span class="price">265.000 €</span><p>Lorem ipsum dolor sit amet, consectetur adipiscing elit, sed do eiusmod</p></article>

<div class="promo-head">SPECIALLY PROMOTED</div>
<div class="promo-photo" style="left:0;width:402px;background:linear-gradient(180deg,#8fb8c8,#b9c7a4 45%,#c7c9c8 70%,#8d8f90)" role="img" aria-label="Bright living room with sofa and sea view windows"></div>
<div class="promo-photo" style="left:800px;width:400px;background:linear-gradient(180deg,#8fb8c8,#b9c7a4 45%,#c7c9c8 70%,#8d8f90)" role="img" aria-label="Living room with sofa overlooking trees and sea"></div>
<div class="promo-panel">
  <h3>4 BED DETACHED<br>VILLA IN LAS CHAPAS</h3>
  <p class="lead">Sed ut perspiciatis unde omnis iste natus error sit voluptatem accusantium doloremque laudantium, totam rem aperiam, eaque ipsa quae</p>
  <p class="facts">beds 4 // baths 6<br>built 255m2 // plot 525m2</p>
  <p class="amount">1.100.000 €</p>
</div>
<svg class="promo-arrow" style="left:30px" viewBox="0 0 24 40"><path d="M18 6L6 20l12 14" stroke="#fff" stroke-width="2" fill="none"/></svg>
<svg class="promo-arrow" style="left:1146px" viewBox="0 0 24 40"><path d="M6 6l12 14L6 34" stroke="#fff" stroke-width="2" fill="none"/></svg>

<h2 class="section-title" style="top:1784px;font-size:25px">HIGHLIGHTED PROPERTIES</h2>
<div class="hl-item" style="left:98px;top:1854px"><div class="thumb" role="img" aria-label="Beach house on stilts" style="background:linear-gradient(180deg,#7fb0de,#6b8a86 60%,#c9b79a)"></div><div class="txt"><h4>Sed ut perspiciatis unde</h4><div class="p">265.000 €</div><div class="d">Lorem ipsum dolor sit amet, consectetur adipiscing elit, sed do eiusmod</div></div></div>
<div class="hl-item" style="left:450px;top:1854px"><div class="thumb" role="img" aria-label="Two storey family house" style="background:linear-gradient(180deg,#9cc1e3,#d8d4cc 55%,#6f7f5a)"></div><div class="txt"><h4>Sed ut perspiciatis unde</h4><div class="p">265.000 €</div><div class="d">Lorem ipsum dolor sit amet, consectetur adipiscing elit, sed do eiusmod</div></div></div>
<div class="hl-item" style="left:800px;top:1854px"><div class="thumb" role="img" aria-label="Wooden house with wide porch" style="background:linear-gradient(180deg,#cfd6dc,#a47c55 55%,#7a6a54)"></div><div class="txt"><h4>Sed ut perspiciatis unde</h4><div class="p">265.000 €</div><div class="d">Lorem ipsum dolor sit amet, consectetur adipiscing elit, sed do eiusmod</div></div></div>
<div class="hl-item" style="left:98px;top:2007px"><div class="thumb" role="img" aria-label="Terrace with infinity pool and sea view" style="background:linear-gradient(180deg,#bcd9ec,#6fa6c8 55%,#3d6c8a)"></div><div class="txt"><h4>Sed ut perspiciatis unde</h4><div class="p">265.000 €</div><div class="d">Lorem ipsum dolor sit amet, consectetur adipiscing elit, sed do eiusmod</div></div></div>
<div class="hl-item" style="left:450px;top:2007px"><div class="thumb" role="img" aria-label="Villa with pool among trees" style="background:linear-gradient(180deg,#98b3c2,#d9d2c3 50%,#4aa0c2)"></div><div class="txt"><h4>Sed ut perspiciatis unde</h4><div class="p">265.000 €</div><div class="d">Lorem ipsum dolor sit amet, consectetur adipiscing elit, sed do eiusmod</div></div></div>
<div class="hl-item" style="left:800px;top:2007px"><div class="thumb" role="img" aria-label="Thatched beach bungalow by turquoise water" style="background:linear-gradient(180deg,#a9d6ea,#3fb4c4 50%,#e6dcc4)"></div><div class="txt"><h4>Sed ut perspiciatis unde</h4><div class="p">265.000 €</div><div class="d">Lorem ipsum dolor sit amet, consectetur adipiscing elit, sed do eiusmod</div></div></div>

<section class="coast" role="img" aria-label="Overview of the Costa del Sol coastline with the sales areas marked">
  <span class="marker" style="left:146px;top:171px">Sed ut pers</span>
  <span class="marker" style="left:475px;top:151px">Sed ut pers</span>
  <span class="marker" style="left:638px;top:114px">Sed ut pers</span>
  <span class="marker" style="left:318px;top:203px">Sed ut pers</span>
  <span class="marker" style="left:722px;top:171px">Sed ut pers</span>
  <span class="marker" style="left:894px;top:169px">Sed ut pers</span>
  <span class="marker" style="left:1056px;top:133px">Sed ut pers</span>
  <span class="marker" style="left:153px;top:240px">Sed ut pers</span>
  <span class="marker" style="left:514px;top:224px">Sed ut perspiciat</span>
  <span class="marker" style="left:988px;top:236px">Sed ut pers</span>
  <span class="marker" style="left:1118px;top:285px">Sed ut pers</span>
  <span class="marker" style="left:679px;top:290px">Sed ut perspiciat</span>
  <span class="marker" style="left:862px;top:287px">Sed ut perspiciat</span>
  <span class="marker" style="left:1045px;top:382px">Sed ut pers</span>
</section>

<section class="news">
  <h2>LATEST NEWS</h2>
  <article class="news-item" style="left:98px">
    <h5>Nemo Enim Ipsam Voluptatem ?</h5><div class="date">Janu 21, 2016</div>
    <p class="body">Duis aute irure dolor in reprehenderit in voluptate velit esse cillum dolore eu fugiat nulla pariatur. Excepteur sint occaecat cupidatat non proident, sunt in culpa qui officia deserunt mollit</p>
    <div class="more"><svg width="11" height="11"><circle cx="5.5" cy="5.5" r="4.5" fill="none" stroke="#555"/><path d="M4.5 3.5l2 2-2 2" stroke="#555" fill="none"/></svg>READ MORE</div>
  </article>
  <article class="news-item" style="left:450px">
    <h5>Nemo Enim Ipsam Voluptatem ?</h5><div class="date">Janu 21, 2016</div>
    <p class="body">Duis aute irure dolor in reprehenderit in voluptate velit esse cillum dolore eu fugiat nulla pariatur. Excepteur sint occaecat cupidatat non proident, sunt in culpa qui officia deserunt mollit</p>
    <div class="more"><svg width="11" height="11"><circle cx="5.5" cy="5.5" r="4.5" fill="none" stroke="#555"/><path d="M4.5 3.5l2 2-2 2" stroke="#555" fill="none"/></svg>READ MORE</div>
  </article>
  <h3 class="testimonial-title">TESTIMONIAL</h3>
  <blockquote class="testimonial">
    <q>Duis aute irure dolor in reprehenderit in voluptate velit esse cillum dolore eu fugiat nulla pariatur. Excepteur sint occaecat cupidatat non proident, sunt in culpa qui officia deserunt mollit anim id est laborum.</q>
    <div class="who">- MARTA LINDQVIST<br>Property Agent</div>
  </blockquote>
  <div class="avatar" role="img" aria-label="Portrait of the property agent"></div>
</section>

<footer class="site-footer">
  <div class="foot-brand"><span class="mark"></span><span class="name">Vela Habitat</span></div>
  <div class="socials"><span></span><span></span><span></span><span></span><span></span></div>
  <div class="foot-col" style="left:386px">
    <h6>CONTACT US</h6>
    <div class="line">Vela Habitat<br>4721 KL Velmaar The Netherlands</div>
    <div class="ico"><svg width="14" height="14"><path d="M3 2c1-1 2-1 2.5 0l1 2c.3.7 0 1.3-.6 1.6-.3.3 0 1.3 1.3 2.6s2.3 1.6 2.6 1.3c.3-.6 1-.9 1.6-.6l2 1c1 .5 1 1.5 0 2.5-1.5 1.5-4 1-7-2S1.5 3.5 3 2z" fill="#fff"/></svg>+1 917 555 0193</div>
    <div class="ico"><svg width="16" height="12"><rect x="1" y="1" width="14" height="10" fill="none" stroke="#fff"/><path d="M1 1l7 6 7-6" stroke="#fff" fill="none"/></svg>info@velahabitat.com</div>
  </div>
  <div class="foot-col" style="left:697px">
    <h6>QUICK LINKS</h6>
    <ul class="quick"><li>Home</li><li>About Us</li><li>Property</li><li>Agent</li><li>Contact Us</li></ul>
  </div>
  <div class="foot-col" style="left:873px">
    <h6>SIGN UP TO RECEIVE EMAIL</h6>
    <div class="line" style="font-size:11.5px">Excepteur sint occaecat cupidatat non<br>proident, sunt in culpa qui</div>
    <div class="email-input">Enter email</div>
    <div class="subscribe">SUBSCRIBE</div>
  </div>
</footer>
<div class="copy-bar">Copyright©2016 Vela Habitat .All Right Reserved</div>

</body>
</html>
```